Business Card for Tutoring Company

We need a logo/symbol for an education company, along with an attractive business card. The logo should resemble both a pi symbol and the letter T.
Updates

Dear Designers,

I am narrowing down what I am looking for. 
I want the front of the card to be primarily white, with the company name "Bright Harbor Learning" positioned towards the center.  The first letter, 'T' in 'Bright' will be modified so that it resembles a Pi symbol.
My personal information will be at the bottom.  If you think it fits, the website can be strewn across the top.

As for the back of the card, it will be primarily blue.  Toward the center will be the same T/pi shape engraved into a circular disk/button/emblem shape with some border.  It should be noted that I do like shiny blue, like the blue face of a Varnel.  Underneath the logo will be white text that reads, "Making Independent Learners and Thinkers."  At the very bottom of the card in smaller white font, the website "BrightHarborLearning.example" is written.

For more clarification, see my recent attachment.

Thank you.

Leonard

Industry/Entity Type

Education

Logo styles of interest
Pictorial/Combination Logo
Requirements
Must have
• LOGO:
The logo is a solid blue circle with a symbol cutout from it. The cut out should closely resemble π and be the color white.

CARD:
The front has the logo in the top left corner, with "BRIGHT HARBOR LEARNING" written out beside it, spanning the width of the card. " At the bottom, personal information can be placed: Name, Title, Phone, Email.
The back has the the logo centered and enlarged. The website is printed "BrightHarborLearning.example
Nice to have
• LOGO:
It would be nice if the logo/pi symbol could be used as a letter T when spelling BHL or Bright Harbor Learning.

CARD:
The enlarged logo on the back of the card can be enhanced (i.e. the blue is not solid blue but shiny, like the metallic blue face of a varnel) It would also be nice if the logo had a cool background (i.e. instead of the cutout of the pi-shape being white, it could be outerspace or something. Also, a motto "Making Independent Learner and Thinkers" printed under "BrightHarborLearning.example" would be nice, if it fits.

```html
<!DOCTYPE html>
<html lang="en">
<head>
<meta charset="utf-8">
<title>Bright Harbor Learning – Business Card Options</title>
<link rel="stylesheet" href="https://fonts.googleapis.com/css2?family=Questrial&family=Montserrat:wght@600&display=swap">
<style>
  :root {
    --page: #ffffff;
    --frame: #c9c9c9;
    --label: #a3a3a3;
    --ink: #2a3c8c;
    --navy: #1f3f8f;
    --band-light: #5fb6ea;
    --band-mid: #0e84d4;
    --band-dark: #1a3a86;
    --card-corner: #c4d3e0;
    --card-center: #ffffff;
  }
  * { margin: 0; padding: 0; box-sizing: border-box; }
  html, body {
    width: 979px;
    height: 1200px;
    overflow: hidden;
    background: var(--page);
  }
  .sheet {
    position: relative;
    width: 979px;
    height: 1200px;
  }
  .sheet-frame {
    position: absolute;
    left: 1px; top: 1px;
    width: 976px; height: 1197px;
    border: 2px solid var(--frame);
  }
  .option-label {
    position: absolute;
    width: 100px;
    margin-left: -50px;
    text-align: center;
    font-family: "Questrial", sans-serif;
    font-size: 96px;
    line-height: 1;
    color: var(--label);
    z-index: 2;
  }
  .option-label.a { left: 489px; top: 22px; }
  .option-label.b { left: 496px; top: 598px; }

  .card {
    position: absolute;
    width: 892px;
    height: 546px;
    overflow: hidden;
    background: radial-gradient(ellipse 62% 70% at 50% 50%, var(--card-center) 55%, var(--card-corner) 100%);
  }
  .card.a { left: 42px; top: 39px; }
  .card.b { left: 49px; top: 620px; }

  .brand {
    position: absolute;
    left: 87px;
    top: 89px;
    display: flex;
    align-items: center;
    gap: 38px;
  }
  .brand-dot {
    width: 124px;
    height: 124px;
    border-radius: 50%;
    background: var(--navy);
  }
  .brand-name {
    font-family: "Montserrat", sans-serif;
    font-weight: 600;
    font-size: 31px;
    letter-spacing: 1.5px;
    color: var(--navy);
    white-space: nowrap;
  }

  .card-band {
    position: absolute;
    left: 0; top: 246px;
    width: 100%;
    height: 20px;
    background: linear-gradient(90deg,
      var(--band-mid) 0%, var(--band-light) 22%, var(--band-mid) 36%,
      var(--band-dark) 52%, var(--band-mid) 66%, var(--band-light) 80%, var(--band-mid) 100%);
  }

  .contact {
    position: absolute;
    top: 350px;
    font-family: "Questrial", sans-serif;
    font-size: 29px;
    line-height: 53px;
    color: var(--ink);
    white-space: pre;
  }
  .contact.person { left: 91px; }
  .contact.role { right: 66px; text-align: left; }
</style>
</head>
<body>
<main class="sheet">
  <div class="sheet-frame"></div>

  <div class="option-label a">a</div>
  <section class="card a">
    <div class="brand">
      <span class="brand-dot"></span>
      <span class="brand-name">BRIGHT HARBOR LEARNING</span>
    </div>
    <div class="card-band"></div>
    <div class="contact person">Leonard Ashby
(555)   014   2273</div>
    <div class="contact role">Education  Consultant
leonard@brightharbor.example</div>
  </section>

  <div class="option-label b">b</div>
  <section class="card b">
    <div class="brand">
      <span class="brand-dot"></span>
      <span class="brand-name">BRIGHT HARBOR LEARNING</span>
    </div>
    <div class="card-band"></div>
    <div class="contact person">Leonard Ashby
(555)   014   2273</div>
    <div class="contact role">Education  Consultant
leonard@brightharbor.example</div>
  </section>
</main>
</body>
</html>
```